Startup fashion company needs high-end, stylish and hip business cards!

We need a business card design that uses a logo that we just completed with a ArtFolkHub artist.

Our company is Velmora. We work with fashion designers to display their designs on our website and handle all back-end fulfillment for them (fabric sourcing, garment manufacturing, customer service, etc.). The word Velmora is a play on fashion trunk shows, where designers will show their wares in a small, intimate setting. The final design should communicate high-end / luxe, chic, stylish, fashion-forward, hip!

We are using greys as our logo color (#2d2d2d, #ababab). We are also interested, for branding purposes and on our website, to use purple as a highlight color (#4a3455). I have the logo in other formats if needed.

Target Market(s)

Investors, customers, fashion designers, suppliers

Industry/Entity Type

Fashion

Contact Information for Business Card

There should be space for:
Name
Title
Address 1
Address 2
City, State Zip
USA
Phone
Email
ChatLine
Chirper

If it makes sense to put one or more of the contact info on the same line, that is fine if it won't be confusing.

Font styles to use
Sans Serif
Other font styles liked:
• Would like the font to be complementary to our logo font/look and feel. The logo font is Caviar Dreams with a stylized 'N' according to the logo designer.

Colors
876aae
e4daea
f3f1f8
ffffff

Requirements
Must have
• The cards will most likely printed through PrintQuay and therefore must meet their upload file guidelines. There are also software templates for business cards that can be utilized. Information below from PrintQuay site.
• We support a variety of file formats for uploaded designs.
• Adobe Acrobat 9 Document (*.pdf) (recommended)
• Adobe Illustrator CS3 Artwork (*.ai) (recommended)
• Adobe Photoshop CS3 Image (*.psd) (recommended)
• Bitmap Image (*.bmp)
• GIF Image (*.gif)
• JPEG Image (*.jpg,*.jpeg)
• Microsoft PowerPoint 2010 Document (*.ppt)
• Microsoft Publisher 2010 Document (*.pub)
• Microsoft Word 2010 Document (*.doc)
• PCX Image (*.pcx)
• PICT Image (*.pic,*.pict,*.pct)
• PNG Image (*.png)
• PostScript Document (*.ps)
• TIFF Image (*.tif,*.tiff)
• Windows Enhanced Metafile (*.emf)
• Windows Metafile (*.wmf)
• The templates on their site:
• Using a downloadable template for your application will ensure that your dimensions, resolution and color settings match ours.
• - Adobe Photoshop (recommended) Download Horizontal Template
• - Adobe Illustrator (recommended) Download Horizontal Template
• If you are creating a PDF document in Acrobat Distiller, please use our Distiller settings.
• - Adobe Acrobat Distiller (recommended) Download Settings
• Sizing:
• Full Bleed Size
• 3.62" x 2.12"
• 92 x 54 mm
• 1085 x 635 pixels
• Document Trim Size
• 3.50" x 2.00"
• 89 x 51 mm
• 1050 x 600 pixels
Nice to have
• The back can use either the full logo or just the elephant or a combination? I'm imagining a full color backside...open to other suggestions!

```html
<!DOCTYPE html>
<html lang="en">
<head>
<meta charset="utf-8">
<title>Velmora Business Card</title>
<link href="https://fonts.googleapis.com/css2?family=Questrial&display=swap" rel="stylesheet">
<style>
  :root {
    --bg: #e4e1dc;
    --card: #ffffff;
    --ink: #2d2d2d;
    --ink-soft: #4a4a4a;
    --grey: #ababab;
    --purple: #876aae;
    --purple-deep: #4a3455;
    --purple-tint: #b9a6d3;
  }
  * { box-sizing: border-box; margin: 0; padding: 0; }
  html, body { width: 1200px; height: 885px; overflow: hidden; }
  body {
    background: var(--bg);
    font-family: "Questrial", "Helvetica Neue", Arial, sans-serif;
    color: var(--ink);
    position: relative;
  }
  .card {
    position: absolute;
    left: 260px;
    width: 680px;
    height: 389px;
    background: var(--card);
    box-shadow: 0 6px 18px rgba(0,0,0,0.18);
  }
  .card--front { top: 30px; }
  .card--back { top: 465px; }

  .brand {
    position: absolute;
    display: flex;
    align-items: center;
  }
  .brand__dot {
    border-radius: 50%;
    background: var(--purple-deep);
    flex: none;
  }
  .brand__name {
    color: var(--ink);
    letter-spacing: 0.04em;
    line-height: 1;
  }
  .card--front .brand { left: 40px; top: 44px; gap: 14px; }
  .card--front .brand__dot { width: 46px; height: 46px; }
  .card--front .brand__name { font-size: 66px; }

  .person { position: absolute; left: 96px; top: 128px; }
  .person__name { font-size: 25px; color: var(--purple); letter-spacing: 0.01em; }
  .person__title { font-size: 17px; color: var(--ink-soft); margin-top: 3px; }

  .contacts { position: absolute; left: 118px; top: 218px; list-style: none; }
  .contacts li {
    display: flex; align-items: center; gap: 12px;
    font-size: 17px; color: var(--ink-soft);
    height: 28px;
  }
  .icon {
    width: 18px; height: 18px; flex: none;
    background: var(--purple-tint);
    border-radius: 2px;
    display: flex; align-items: center; justify-content: center;
  }
  .icon svg { width: 12px; height: 12px; }

  .divider {
    position: absolute; left: 400px; top: 200px;
    width: 1.5px; height: 110px; background: var(--ink);
  }
  .address { position: absolute; left: 438px; top: 214px; font-size: 16px; color: var(--ink-soft); line-height: 26px; }
  .address__city { display: flex; align-items: center; gap: 10px; }

  .card--back .brand { left: 0; right: 0; top: 0; bottom: 0; justify-content: center; gap: 18px; }
  .card--back .brand__dot { width: 62px; height: 62px; }
  .card--back .brand__name { font-size: 92px; }
</style>
</head>
<body>
  <section class="card card--front" aria-label="Business card front">
    <div class="brand">
      <span class="brand__dot"></span>
      <span class="brand__name">VELMORA</span>
    </div>

    <div class="person">
      <p class="person__name">Employee Name</p>
      <p class="person__title">Managing Director</p>
    </div>

    <ul class="contacts">
      <li><span class="icon"><svg viewBox="0 0 12 12"><path d="M3 1 L5 3.5 L4 5 Q5 7 7 8 L8.5 7 L11 9 L9.5 11 Q2 9.5 1 2.5 Z" fill="#fff"/></svg></span>0012 3456 789</li>
      <li><span class="icon"><svg viewBox="0 0 12 12"><rect x="1" y="3" width="10" height="7" fill="none" stroke="#fff" stroke-width="1.3"/><path d="M1 3 L6 7 L11 3" fill="none" stroke="#fff" stroke-width="1.3"/></svg></span>info@velmora-mail.com</li>
      <li><span class="icon"></span>Your ChatLine Address</li>
      <li><span class="icon"></span>Your Chirper Address</li>
    </ul>

    <div class="divider"></div>

    <div class="address">
      <p>Your Adress Inc 2nd Lane</p>
      <p>Ave Larkfield, NJ 00000</p>
      <p class="address__city"><span class="icon"><svg viewBox="0 0 12 12"><path d="M6 11 Q2 6.5 2 4.5 A4 4 0 0 1 10 4.5 Q10 6.5 6 11 Z" fill="#fff"/><circle cx="6" cy="4.5" r="1.4" fill="var(--purple-tint)"/></svg></span>City, State Zip USA</p>
    </div>
  </section>

  <section class="card card--back" aria-label="Business card back">
    <div class="brand">
      <span class="brand__dot"></span>
      <span class="brand__name">VELMORA</span>
    </div>
  </section>
</body>
</html>
```